Divorce Lawyer Creative Business Card Design Project

Need a fresh look for our business cards that incorporates our current logo. We have three attorneys and six staff. Some will also use a Q/R Code (which is personal to the staff member) and that should be incorporated into the design so that we have a "with Q/R Code option" and a "without Q/R Code option"
While our business is serious and we want to be professional, we also welcome a bit of creativity and "fun." See http://cardowlet.example/creative-business-card-for-a-divorce-lawyer/ for a unique divorce lawyer business card. It is cool but the card itself is boring...
We add new people, change titles, some of our staff get married (and divorced) and have name changes and we need the ability to use a design template that you provide to make these changes ourselves. We usually print our cards at Plumo Press.
I have uploaded a file that contains a sample of our current front and back of the business card as well as a sample Q/R Contact code to be included on a card. Obviously, we like the design that we have which should give you a feel for us but we are ready for a fresh look.
If you can't provide a design that we can manipulate, we will need .eps, .pdf, and .jpg files for three attorneys and six staff.
Updates
- Layout for this card is really nice: http://blog.inkhollow.example/wp-content/uploads/2013/03/torva-business-card.jpg
- This is creative: http://pinboardly.example/pin/572810394628150443/ but I don't really like it.
- Plastic is kind of cool: http://pinboardly.example/pin/572810394628937216/
- DISLIKE: http://promoglobe.example/sites/default/files/styles/media/public/images/Lawyerbusinesscard.jpg?itok=ZrTmWe-k
- This is really cool but I fear the printing costs would be too high: http://pinboardly.example/pin/46192837504618352/
- I am not opposed to different but similar designs: See http://www.folioverse.example/gallery/ZEP-Business-Cards/8263045
Industry/Entity Type
Lawyer
Requirements
Must have
- Our Logo
Person's Full Name
Title
Phone #
Fax #
Email
Web Address

```html
<!DOCTYPE html>
<html lang="en">
<head>
<meta charset="utf-8">
<title>Divorce Lawyer Business Cards and Letterhead</title>
<link href="https://fonts.googleapis.com/css2?family=Open+Sans:wght@300;400;700&display=swap" rel="stylesheet">
<style>
  :root {
    --teal: #07b8bb;
    --lime: #b5d334;
    --white: #ffffff;
    --ink: #1a1a1a;
    --grey-text: #9a9a9a;
    --stage: #3a3a3c;
    --edge: #d0d0d0;
  }
  * { box-sizing: border-box; margin: 0; padding: 0; }
  html, body { width: 1200px; height: 900px; overflow: hidden; }
  body {
    position: relative;
    background: var(--stage);
    font-family: "Open Sans", sans-serif;
  }

  /* Letterhead */
  .letterhead {
    position: absolute;
    left: 60px; top: 125px;
    width: 460px; height: 650px;
    background: var(--white);
    box-shadow: 0 4px 14px rgba(0,0,0,0.3);
    overflow: hidden;
  }
  .letterhead__band {
    position: absolute;
    left: 0; top: 70px;
    width: 250px; height: 46px;
    background: var(--lime);
    color: var(--white);
    font-size: 17px;
    font-weight: 300;
    line-height: 46px;
    padding-left: 40px;
  }
  .letterhead__bar {
    position: absolute;
    left: 250px; top: 40px;
    width: 12px; height: 190px;
    background: var(--teal);
  }
  .letterhead__rule {
    position: absolute;
    left: 262px; top: 150px;
    width: 150px;
    border-top: 2px dashed var(--teal);
  }
  .letterhead__footer {
    position: absolute;
    left: 0; right: 0; bottom: 34px;
    text-align: center;
    font-size: 10px;
    font-weight: 300;
    color: var(--grey-text);
  }
  .letterhead__footer .divider { margin: 0 8px; }
  .letterhead__footer .site { color: var(--ink); }
  .letterhead__footer .site em { font-style: normal; color: var(--lime); }

  /* Cards */
  .card {
    position: absolute;
    width: 220px;
    height: 385px;
    border-radius: 26px 0 26px 0;
    overflow: hidden;
    box-shadow: 0 4px 14px rgba(0,0,0,0.3);
  }
  .card--teal { background: var(--teal); color: var(--white); }
  .card--white { background: var(--white); color: var(--ink); }
  .pos-a { left: 580px; top: 45px; }
  .pos-b { left: 840px; top: 45px; }
  .pos-c { left: 580px; top: 470px; }
  .pos-d { left: 840px; top: 470px; }

  .card__tab {
    position: absolute;
    top: 0; left: 0;
    width: 135px; height: 14px;
  }
  .card--teal .card__tab { background: var(--white); }
  .card--white .card__tab { background: var(--teal); }

  .card__rule {
    position: absolute;
    left: 64px; top: 14px; bottom: 0;
    border-left: 2px dashed var(--white);
  }
  .card--white .card__rule { border-left-color: var(--teal); bottom: 34px; }

  .headline {
    position: absolute;
    top: 78px; left: 0;
    width: 100%; height: 22px;
    font-size: 17px;
    line-height: 22px;
  }
  .headline__light {
    position: absolute;
    right: 162px;
    font-weight: 300;
  }
  .headline__bold {
    position: absolute;
    left: 72px;
    font-weight: 700;
    letter-spacing: 0.4px;
  }
  .card--white .headline__light { color: var(--teal); }
  .card--white .headline__bold { color: var(--lime); }

  .person {
    position: absolute;
    left: 92px; top: 215px;
  }
  .person__name { font-size: 12.5px; font-weight: 400; white-space: nowrap; }
  .person__title { font-size: 9px; font-weight: 300; margin-top: 3px; padding-left: 8px; }

  .back__rule-top { bottom: auto; height: 118px; }
  .back__rule-bottom { top: 222px; bottom: 0; }
  .contact {
    position: absolute;
    top: 142px; left: 0;
    width: 100%;
    text-align: center;
    font-size: 8.5px;
    font-weight: 300;
    font-style: normal;
    line-height: 1.65;
  }

  .back-white__bar {
    position: absolute;
    left: 22px; top: 40px;
    width: 10px; height: 250px;
    background: var(--teal);
  }
  .back-white__rule {
    position: absolute;
    left: 32px; top: 175px;
    width: 130px;
    border-top: 2px dashed var(--teal);
  }
  .card--white .contact { color: var(--lime); top: 70px; padding-left: 30px; }
</style>
</head>
<body>
  <section class="letterhead" aria-label="Letterhead">
    <div class="letterhead__band">Managing Attorney</div>
    <div class="letterhead__bar"></div>
    <div class="letterhead__rule"></div>
    <p class="letterhead__footer">Suite B, 218 Linden street, Marlow NC 28190<span class="divider">|</span><span class="site">www.<em>hollowayfamily</em>.example</span></p>
  </section>

  <section class="card card--teal pos-a" aria-label="Card front, teal">
    <div class="card__tab"></div>
    <div class="card__rule"></div>
    <h1 class="headline"><span class="headline__light">Divorce</span><span class="headline__bold">LAWYER</span></h1>
    <div class="person">
      <p class="person__name">Daniel Reeve Hollis</p>
      <p class="person__title">Managing Attorney</p>
    </div>
  </section>

  <section class="card card--white pos-b" aria-label="Card front, white">
    <div class="card__tab"></div>
    <div class="card__rule"></div>
    <h1 class="headline"><span class="headline__light">Divorce</span><span class="headline__bold">LAWYER</span></h1>
    <div class="person">
      <p class="person__name">Daniel Reeve Hollis</p>
      <p class="person__title">Managing Attorney</p>
    </div>
  </section>

  <section class="card card--teal pos-c" aria-label="Card back, teal">
    <div class="card__tab"></div>
    <div class="card__rule back__rule-top"></div>
    <div class="card__rule back__rule-bottom"></div>
    <address class="contact">
      Harbor Court-Suite B 218 Linden street<br>
      Marlow, NC 28190<br>
      Phone - 910 555 0147 | Email -<br>
      dhollis@hollowayfamily.example
    </address>
  </section>

  <section class="card card--white pos-d" aria-label="Card back, white">
    <div class="back-white__bar"></div>
    <div class="back-white__rule"></div>
    <address class="contact">
      Harbor Court-Suite B 218 Linden street<br>
      Marlow, NC 28190<br>
      Phone - 910 555 0147 | Email -<br>
      dhollis@hollowayfamily.example
    </address>
  </section>
</body>
</html>
```